Heating and Air Conditioning Company Needs a Business Card Design

Need a business card design for a company in South Carolina called "Larkfield Heating & Cooling LLC". We install, maintain, and repair HVAC systems and the bulk of our business is residential. We have a logo and are looking for a clean, professional looking card that resonates with "setting the standard for service and comfort".
Updates
Forgot to include this info - Licensed & Insured

Industry/Entity Type
Business

```html
<!DOCTYPE html>
<html lang="en">
<head>
<meta charset="utf-8">
<title>Larkfield Heating &amp; Cooling LLC – Business Card</title>
<link rel="stylesheet" href="https://fonts.googleapis.com/css2?family=Source+Sans+3:wght@400;600;700&display=swap">
<style>
  :root {
    --backdrop: #d8d5d0;
    --card: #222223;
    --card-edge: #2a2a2b;
    --ink-white: #f2f2f2;
    --ink-soft: #c9c9c9;
    --ink-muted: #b3b3b3;
    --emboss: #3a3a3c;
    --accent-red: #e3262b;
    --accent-blue: #2c62c2;
    --font: "Source Sans 3", "Segoe UI", Arial, sans-serif;
  }
  * { box-sizing: border-box; margin: 0; padding: 0; }
  html, body { width: 1200px; height: 1000px; overflow: hidden; }
  body { background: var(--backdrop); font-family: var(--font); position: relative; }

  .card {
    position: absolute;
    left: 265px;
    width: 667px;
    height: 398px;
    background: var(--card);
    border: 1px solid var(--card-edge);
    box-shadow: 0 6px 16px rgba(0,0,0,0.25);
  }
  .card--front { top: 73px; }
  .card--back { top: 532px; }

  /* Front */
  .front-wordmark {
    position: absolute;
    left: 0; right: 0; top: 168px;
    text-align: center;
    color: var(--emboss);
    font-weight: 700;
    font-size: 44px;
    line-height: 1.1;
    letter-spacing: 0.5px;
  }

  /* Back */
  .brand {
    position: absolute;
    left: 28px; top: 164px;
    width: 320px;
    text-align: center;
  }
  .brand__name {
    display: inline-flex;
    align-items: center;
    gap: 10px;
    color: var(--ink-white);
    font-weight: 700;
    font-size: 25px;
    line-height: 1.1;
  }
  .brand__dot {
    width: 22px; height: 22px;
    border-radius: 50%;
    background: var(--accent-blue);
    flex: none;
  }
  .brand__sub {
    display: block;
    color: var(--ink-white);
    font-weight: 700;
    font-size: 17px;
    margin-top: 2px;
  }
  .licensed {
    position: absolute;
    left: 28px; top: 240px;
    width: 320px;
    text-align: center;
    color: var(--ink-muted);
    font-size: 16px;
  }

  .person { position: absolute; left: 374px; top: 44px; }
  .person__name { color: var(--accent-red); font-weight: 700; font-size: 20px; line-height: 1.15; }
  .person__title { color: var(--ink-white); font-size: 15.5px; line-height: 1.2; }

  .contact-list { position: absolute; left: 378px; top: 132px; list-style: none; }
  .contact-list li {
    display: flex;
    align-items: flex-start;
    color: var(--ink-white);
    font-size: 16px;
    line-height: 24px;
  }
  .contact-list li + li { margin-top: 0; }
  .contact-list .gap { margin-top: 3px; }
  .contact-icon { width: 14px; height: 14px; margin: 5px 6px 0 0; fill: var(--accent-blue); flex: none; }

  .services {
    position: absolute;
    left: 0; right: 0; top: 343px;
    text-align: center;
    color: var(--ink-soft);
    font-size: 16.5px;
  }
</style>
</head>
<body>

  <section class="card card--front" aria-label="Card front">
    <div class="front-wordmark">Larkfield<br>Heating &amp; Cooling LLC</div>
  </section>

  <section class="card card--back" aria-label="Card back">
    <div class="brand">
      <span class="brand__name"><span class="brand__dot"></span>Larkfield</span>
      <span class="brand__sub">Heating &amp; Cooling LLC</span>
    </div>
    <p class="licensed">Licensed &amp; Insured</p>

    <div class="person">
      <p class="person__name">Dale Pruitt</p>
      <p class="person__title">Certified Technician</p>
    </div>

    <ul class="contact-list">
      <li>
        <svg class="contact-icon" viewBox="0 0 14 14" aria-hidden="true"><path d="M4 0h6a1 1 0 0 1 1 1v12a1 1 0 0 1-1 1H4a1 1 0 0 1-1-1V1a1 1 0 0 1 1-1zm0.5 1.5v10h5v-10z"/></svg>
        (864) 555-0148
      </li>
      <li>
        <svg class="contact-icon" viewBox="0 0 14 14" aria-hidden="true"><path d="M1 4c0-2 2-3 6-3s6 1 6 3v1.5h-3V4H4v1.5H1zM3 7h8l2 6H1z"/></svg>
        (864) 555-0163
      </li>
      <li>
        <svg class="contact-icon" viewBox="0 0 14 14" aria-hidden="true"><path d="M3 0h8v4H3zM1 5h12v6h-2v3H3v-3H1zm3 4v4h6V9z"/></svg>
        (864) 555-0179
      </li>
      <li class="gap">
        <svg class="contact-icon" viewBox="0 0 14 14" aria-hidden="true"><path d="M0 3h14v1L7 8 0 4zM0 5.5l7 4 7-4V12H0z"/></svg>
        dale@larkfieldhc.net
      </li>
      <li class="gap">
        <svg class="contact-icon" viewBox="0 0 14 14" aria-hidden="true"><path d="M7 0a7 7 0 1 0 0 14A7 7 0 0 0 7 0zm0 1.3c.8 0 1.8 1.9 2 4.9H5c.2-3 1.2-4.9 2-4.9zM1.4 6.2h2.3c.1-1.8.4-3.3 1-4.3a5.7 5.7 0 0 0-3.3 4.3zm7.9-4.3c.6 1 .9 2.5 1 4.3h2.3a5.7 5.7 0 0 0-3.3-4.3zM1.4 7.8a5.7 5.7 0 0 0 3.3 4.3c-.6-1-.9-2.5-1-4.3zm3.6 0c.2 3 1.2 4.9 2 4.9s1.8-1.9 2-4.9zm5.3 0c-.1 1.8-.4 3.3-1 4.3a5.7 5.7 0 0 0 3.3-4.3z"/></svg>
        www.larkfieldhc.net
      </li>
      <li class="gap">
        <svg class="contact-icon" viewBox="0 0 14 14" aria-hidden="true"><path d="M7 0a5 5 0 0 1 5 5c0 3.5-5 9-5 9S2 8.5 2 5a5 5 0 0 1 5-5zm0 3a2 2 0 1 0 0 4 2 2 0 0 0 0-4z"/></svg>
        <span>42 Alder Bend Road,<br>Greenwood, SC 29646</span>
      </li>
    </ul>

    <p class="services">Heating • Cooling • Plumbing • Residential • Commercial • Industrial</p>
  </section>

</body>
</html>
```